The Perfect Business Card for Vantorell

I am looking for a business card which beautifully incorporates my logo, reflects my business and looks special, elegant and clean.

```html
<!DOCTYPE html>
<html lang="en">
<head>
<meta charset="utf-8">
<title>Vantorell Business Card</title>
<link href="https://fonts.googleapis.com/css2?family=Cormorant+Garamond:wght@500;600&family=Arimo:ital,wght@0,400;1,400&display=swap" rel="stylesheet">
<style>
  :root {
    --backdrop: #1e1e1e;
    --paper: #fbfbf9;
    --green: #6f9e2c;
    --green-dark: #4e7a1f;
    --green-light: #86b23c;
    --ink: #3c3c3c;
  }
  * { margin: 0; padding: 0; box-sizing: border-box; }
  html, body {
    width: 1200px; height: 874px; overflow: hidden;
    background: var(--backdrop);
  }
  .canvas {
    position: relative; width: 1200px; height: 874px;
    display: flex; flex-direction: column; align-items: center; justify-content: center; gap: 36px;
  }
  .card {
    position: relative; width: 660px; height: 378px;
    background: var(--paper);
  }
  .card-frame {
    position: absolute; inset: 16px;
    border: 2px solid var(--green);
  }
  /* Front */
  .brand {
    position: absolute; inset: 0;
    display: flex; align-items: center; justify-content: center; gap: 18px;
  }
  .brand-dot {
    width: 30px; height: 30px; border-radius: 50%;
    background: var(--green);
  }
  .brand-name {
    font-family: "Cormorant Garamond", serif;
    font-weight: 600; font-size: 62px; letter-spacing: 2px;
    color: var(--green); text-transform: uppercase;
  }
  /* Back */
  .identity {
    position: absolute; left: 92px; top: 142px; width: 200px;
    text-align: right;
  }
  .person-name {
    font-family: "Cormorant Garamond", serif;
    font-weight: 600; font-size: 27px; letter-spacing: 0.5px;
    color: var(--green-dark); text-transform: uppercase; white-space: nowrap;
  }
  .person-title {
    font-family: "Arimo", sans-serif; font-style: italic;
    font-size: 13px; color: var(--green-light); margin-top: -2px;
  }
  .mark-dot {
    position: absolute; left: 312px; top: 168px;
    width: 14px; height: 14px; border-radius: 50%;
    background: var(--green);
  }
  .contacts {
    position: absolute; left: 348px; top: 140px;
    list-style: none;
    font-family: "Arimo", sans-serif; font-size: 13px; line-height: 17px; color: var(--ink);
  }
  .contacts li { display: flex; align-items: flex-start; gap: 8px; margin-bottom: 4px; }
  .contacts svg { width: 11px; height: 11px; margin-top: 3px; flex: none; fill: var(--green); }
</style>
</head>
<body>
<main class="canvas">
  <section class="card card-front">
    <div class="card-frame"></div>
    <div class="brand">
      <span class="brand-dot"></span>
      <span class="brand-name">Vantorell</span>
    </div>
  </section>

  <section class="card card-back">
    <div class="card-frame"></div>
    <div class="identity">
      <p class="person-name">Daniel Harrow</p>
      <p class="person-title">President</p>
    </div>
    <span class="mark-dot"></span>
    <ul class="contacts">
      <li>
        <svg viewBox="0 0 12 12"><path d="M6 0a4 4 0 0 0-4 4c0 3 4 8 4 8s4-5 4-8a4 4 0 0 0-4-4zm0 5.5A1.5 1.5 0 1 1 6 2.5a1.5 1.5 0 0 1 0 3z"/></svg>
        <span>4120 Willow Crest Road<br>Juneau, Alaska 34511</span>
      </li>
      <li>
        <svg viewBox="0 0 12 12"><path d="M2.5 0.5l2 0 1 3-1.4 1a7 7 0 0 0 3.4 3.4l1-1.4 3 1v2a1.5 1.5 0 0 1-1.5 1.5A10 10 0 0 1 1 2a1.5 1.5 0 0 1 1.5-1.5z"/></svg>
        <span>555-318-2046</span>
      </li>
      <li>
        <svg viewBox="0 0 12 12"><path d="M3 0h6a1 1 0 0 1 1 1v10a1 1 0 0 1-1 1H3a1 1 0 0 1-1-1V1a1 1 0 0 1 1-1zm0.5 1.5v8h5v-8z"/></svg>
        <span>555-742-6190</span>
      </li>
      <li>
        <svg viewBox="0 0 12 12"><path d="M0 2h12v8H0zM1 3v.4l5 3.3 5-3.3V3z"/></svg>
        <span>harrow@vantorell.com</span>
      </li>
      <li>
        <svg viewBox="0 0 12 12"><circle cx="6" cy="6" r="6"/></svg>
        <span>www.vantorell.com</span>
      </li>
    </ul>
  </section>
</main>
</body>
</html>
```